SilverLedgerOak - Double Sided Business Card

We are looking for design options or our business cards. We are a Business Solutions and HR solutions Provider - the theme is business, for this card.

Our brand colours are represented within our logo.

Details needed to be put on the front of the business card are:

Employees name: [Sample Name]
Role: [Sample Role]

Address: Suite 4 - Level 3/48 Halloran Avenue Parramatta NSW 2150
M: 0000 000 000
P: 1300 847 213
F: 1300 847 286
E: sample@silverledgeroak.com.au
www.silverledgeroak.com.au
Updates

Reason: Hello, could we please increase our deadline by 5 days. Thanking you, Tess

Target Market(s)

Business Owners, also Candidates looking for Employment

Industry/Entity Type

Business

Contact Information for Business Card

Role: [Sample Role]

M: 0000 000 000
P: 1300 847 213
F: 1300 847 286

Font styles to use
Sans Serif

Colors
3276b5
3176b5
0455a3
85abd2
cfdeed
ffffff
000000
1b1b1b
757575

Requirements
Must have
• Details needed to be put on the front of the business card are:
• Employees name: [Sample Name]
• Role: [Sample Role]
• Address: Suite 4 - Level 3/48 Halloran Avenue Parramatta NSW 2150
• M: 0000 000 000
• P: 1300 847 213
• F: 1300 847 286
• E: sample@silverledgeroak.com.au
• www.silverledgeroak.com.au
Nice to have
• Simplicity, clean and professional.

```html
<!DOCTYPE html>
<html lang="en">
<head>
<meta charset="utf-8">
<title>SilverLedgerOak – Business Card Front</title>
<link href="https://fonts.googleapis.com/css2?family=Lato:wght@400;700;900&display=swap" rel="stylesheet">
<style>
  :root {
    --stage: #d9dadc;
    --card: #eef1f4;
    --navy: #1b2a4a;
    --brand-blue: #0455a3;
    --mid-blue: #3176b5;
    --ink: #1b1b1b;
    --soft-grey: #757575;
    --band-text: #cfdeed;
    --rule: #2a3f7a;
  }
  html, body {
    margin: 0;
    padding: 0;
    width: 1200px;
    height: 970px;
    overflow: hidden;
    background: var(--stage);
    font-family: "Lato", Arial, sans-serif;
  }
  .card {
    position: absolute;
    left: 100px;
    top: 199px;
    width: 1000px;
    height: 572px;
    background: var(--card);
    box-shadow: 0 14px 40px rgba(0,0,0,0.18);
    overflow: hidden;
  }
  .brand {
    position: absolute;
    left: 60px;
    top: 190px;
    width: 370px;
    text-align: center;
  }
  .brand-mark {
    width: 58px;
    height: 58px;
    margin: 0 auto 22px;
    background: var(--brand-blue);
  }
  .brand-name {
    font-weight: 900;
    font-size: 37px;
    color: var(--navy);
    letter-spacing: -0.5px;
    line-height: 1;
  }
  .brand-tagline {
    margin-top: 14px;
    font-weight: 700;
    font-size: 13.5px;
    color: var(--ink);
    white-space: nowrap;
  }
  .divider {
    position: absolute;
    left: 475px;
    top: 130px;
    width: 2px;
    height: 308px;
    background: var(--rule);
  }
  .details {
    position: absolute;
    left: 520px;
    top: 128px;
  }
  .person-name {
    font-weight: 900;
    font-size: 37px;
    color: var(--ink);
    line-height: 1.1;
    letter-spacing: -0.3px;
  }
  .person-role {
    font-size: 27px;
    color: var(--navy);
    line-height: 1.1;
  }
  .address {
    margin-top: 14px;
    font-size: 26px;
    color: var(--ink);
    line-height: 1.3;
  }
  .contact-list {
    list-style: none;
    margin: 14px 0 0;
    padding: 0;
  }
  .contact-item {
    display: flex;
    align-items: center;
    font-size: 26px;
    color: var(--ink);
    height: 34px;
  }
  .contact-icon {
    width: 30px;
    height: 30px;
    margin-right: 10px;
    flex: none;
  }
  .footer-bands {
    position: absolute;
    left: 0;
    bottom: 0;
    width: 1000px;
    height: 60px;
  }
  .website {
    position: absolute;
    right: 50px;
    bottom: 14px;
    font-size: 23px;
    color: var(--band-text);
    letter-spacing: 0.2px;
  }
</style>
</head>
<body>
  <section class="card">
    <div class="brand">
      <div class="brand-mark"></div>
      <div class="brand-name">SilverLedgerOak</div>
      <div class="brand-tagline">Guiding growing firms towards their next big milestone</div>
    </div>

    <div class="divider"></div>

    <div class="details">
      <div class="person-name">LIAM PORTER</div>
      <div class="person-role">Manager</div>
      <div class="address">Level 3/48 Halloran Avenue<br>Kellbrook NSW 2163</div>
      <ul class="contact-list">
        <li class="contact-item">
          <svg class="contact-icon" viewBox="0 0 30 30" aria-hidden="true">
            <circle cx="15" cy="15" r="13" fill="none" stroke="#1b2a4a" stroke-width="2"/>
            <rect x="10.5" y="7" width="9" height="16" rx="1.5" fill="none" stroke="#1b2a4a" stroke-width="1.8"/>
            <circle cx="15" cy="20.3" r="0.9" fill="#1b2a4a"/>
          </svg>0000 000 000
        </li>
        <li class="contact-item">
          <svg class="contact-icon" viewBox="0 0 30 30" aria-hidden="true">
            <circle cx="15" cy="15" r="13" fill="none" stroke="#1b2a4a" stroke-width="2"/>
            <path d="M8 12 q7 -5 14 0 l-1.5 2.5 h-2.5 l-0.5 -2 h-5 l-0.5 2 h-2.5 z" fill="#1b2a4a"/>
            <rect x="9.5" y="15" width="11" height="7" rx="1.5" fill="#1b2a4a"/>
          </svg>1300 847 213
        </li>
        <li class="contact-item">
          <svg class="contact-icon" viewBox="0 0 30 30" aria-hidden="true">
            <circle cx="15" cy="15" r="13" fill="none" stroke="#1b2a4a" stroke-width="2"/>
            <rect x="10.5" y="7.5" width="9" height="5" fill="#1b2a4a"/>
            <rect x="8" y="12" width="14" height="7" rx="1.5" fill="#1b2a4a"/>
            <rect x="10.5" y="17" width="9" height="5.5" fill="#eef1f4" stroke="#1b2a4a" stroke-width="1.5"/>
          </svg>1300 847 286
        </li>
        <li class="contact-item">
          <svg class="contact-icon" viewBox="0 0 30 30" aria-hidden="true">
            <circle cx="15" cy="15" r="13" fill="none" stroke="#1b2a4a" stroke-width="2"/>
            <rect x="8" y="10" width="14" height="10" rx="1" fill="#1b2a4a"/>
            <path d="M8.5 10.5 L15 16 L21.5 10.5" fill="none" stroke="#eef1f4" stroke-width="1.4"/>
          </svg>sample@silverledgeroak.com.au
        </li>
      </ul>
    </div>

    <svg class="footer-bands" viewBox="0 0 1000 60" preserveAspectRatio="none" aria-hidden="true">
      <defs>
        <linearGradient id="bandBlue" x1="0" y1="0" x2="1" y2="0">
          <stop offset="0" stop-color="#1b3d7c"/>
          <stop offset="0.55" stop-color="#24488c"/>
          <stop offset="1" stop-color="#1a3270"/>
        </linearGradient>
      </defs>
      <polygon points="0,4 558,4 548,13 0,13" fill="#1b2a3e"/>
      <polygon points="0,22 560,22 592,0 1000,0 1000,60 0,60" fill="url(#bandBlue)"/>
    </svg>
    <div class="website">www.silverledgeroak.com.au</div>
  </section>
</body>
</html>
```